Simple elegant business card

General card for a fin and television director.
Just want name, email, phone and address.

Target Market(s)

Prospective employers

Industry/Entity Type

Business

Requirements
Must have
• As above
Nice to have
• Logo but not necessary.
Should not have
• Not too colourful or funky.
• Simplicity and elegance the way to go.

```html
<!DOCTYPE html>
<html lang="en">
<head>
<meta charset="utf-8">
<title>Nora Vale — Business Cards</title>
<link rel="stylesheet" href="https://fonts.googleapis.com/css2?family=Jost:wght@400;500&display=swap">
<style>
  :root {
    --stage: #1b2f5e;
    --card-dark: #212326;
    --card-light: #e4e7f2;
    --name-on-dark: #c4c7cc;
    --contact-on-dark: #a9acb1;
    --name-on-light: #6e7178;
    --contact-on-light: #8a8d94;
  }
  * { margin: 0; padding: 0; box-sizing: border-box; }
  html, body {
    width: 1200px;
    height: 900px;
    overflow: hidden;
    background: var(--stage);
    font-family: "Jost", sans-serif;
  }
  .stage {
    width: 1200px;
    height: 900px;
    display: flex;
    flex-direction: column;
    align-items: center;
    justify-content: center;
    gap: 48px;
  }
  .card {
    position: relative;
    width: 640px;
    height: 366px;
    box-shadow: 0 10px 30px rgba(0, 0, 0, 0.35);
  }
  .card--front { background: var(--card-dark); }
  .card--back { background: var(--card-light); }

  .name {
    font-weight: 500;
    font-size: 30px;
    letter-spacing: 1px;
    line-height: 1;
    white-space: nowrap;
  }
  .contact {
    font-weight: 400;
    font-size: 19px;
    letter-spacing: 0.3px;
    line-height: 1;
    white-space: nowrap;
  }
  .contact .divider { margin: 0 10px; opacity: 0.7; }

  .card--front .name {
    position: absolute;
    left: 44px;
    top: 152px;
    color: var(--name-on-dark);
  }
  .card--front .contact {
    position: absolute;
    left: 44px;
    bottom: 44px;
    color: var(--contact-on-dark);
  }

  .card--back .footer {
    position: absolute;
    left: 44px;
    right: 44px;
    bottom: 44px;
    display: flex;
    align-items: baseline;
    gap: 44px;
  }
  .card--back .name { color: var(--name-on-light); }
  .card--back .contact { color: var(--contact-on-light); }
</style>
</head>
<body>
  <main class="stage">
    <section class="card card--front" aria-label="Business card, front">
      <h1 class="name">Nora Vale</h1>
      <p class="contact">+1 310 555 0142<span class="divider">/</span>noravale@mail.com</p>
    </section>
    <section class="card card--back" aria-label="Business card, back">
      <div class="footer">
        <h2 class="name">Nora Vale</h2>
        <p class="contact">+1 310 555 0142<span class="divider">/</span>noravale@mail.com</p>
      </div>
    </section>
  </main>
</body>
</html>
```